7BrightHarbor.com - website redesign

We need to redesign 7BrightHarbor.com.
Here are design specs: https://files.example-share.net/deck/8kfQz2LmWp4RtY6NvB3xHcJd9SaE1uTg0oKiZnMb/view

Here is a video going over the design specs:
https://media.example-vault.net/clip/9Rw3TzQp0LmXk7VbNc2Hd5SfJ-/watch

Target Market(s)

Seattle, WA

Number of Pages Required

2 page

Font styles to use
Serif

Colors

Designer to choose colors to be used in the design.

Requirements
Must have
• Desktop and Mobile Designs
Use colors from their logo....as provided in the design specs document.

Should not have
• Please follow design specs as provided in Google Slides. Must watch the video to understand what's needed.

```html
<!DOCTYPE html>
<html lang="en">
<head>
<meta charset="utf-8">
<title>7 Bright Harbor – Certified E-Recycling</title>
<link href="https://fonts.googleapis.com/css2?family=Tinos:wght@400;700&display=swap" rel="stylesheet">
<style>
:root{
  --green:#47a93a;
  --green-dark:#3a8f2f;
  --lime:#8fd14f;
  --ink:#3b3b3b;
  --muted:#7a7a7a;
  --line:#e3e3e3;
  --footer:#3c3c3c;
  --footer-deep:#2f2f2f;
  --white:#ffffff;
  --map-a:#e7ede0;
  --map-b:#d5e4c4;
}
*{box-sizing:border-box;margin:0;padding:0}
html,body{width:1200px;height:4642px;overflow:hidden}
body{font-family:"Tinos","Times New Roman",serif;color:var(--ink);background:var(--white);position:relative}
section,header,nav,footer{position:absolute;left:0;width:1200px}
.abs{position:absolute}
.btn{position:absolute;display:flex;align-items:center;justify-content:center;font-size:12px;text-transform:uppercase;color:var(--white);background:var(--green);white-space:nowrap}

/* header */
.site-header{top:0;height:125px;background:var(--white)}
.brand{left:155px;top:42px;display:flex;align-items:center;gap:8px}
.brand-dot{width:30px;height:30px;border-radius:50%;background:var(--green)}
.brand-name{font-size:22px;font-weight:700;color:var(--green)}
.top-btn{top:45px;width:150px;height:40px}
.top-btn.phone{background:var(--white);border:2px solid var(--green);color:var(--green);gap:8px;text-transform:none}
.main-nav{top:125px;height:39px;background:var(--green)}
.main-nav ul{list-style:none;display:flex;gap:34px;position:absolute;left:155px;top:12px;font-size:12px;color:var(--white)}
.live-chat{left:920px;top:0;width:125px;height:39px;background:var(--lime);text-transform:none;gap:8px}

/* hero */
.hero{top:164px;height:470px}
.hero-photo{position:absolute;inset:0;background:radial-gradient(circle at 70% 45%,#9fcf6a 0,#5f8f3a 30%,#3d5a26 60%,#2f3f1c 100%)}
.hero-copy{left:157px;top:142px;color:var(--white)}
.hero-copy .l1{font-size:30px;font-weight:700;color:var(--lime);line-height:1}
.hero-copy .l2{font-size:46px;font-weight:700;line-height:1.05}
.hero-copy .l3{font-size:30px;font-weight:700;color:var(--lime);line-height:1}
.hero-copy .tag{font-size:14px;margin-top:6px}
.hero-btn{left:157px;top:274px;width:175px;height:34px;gap:8px}

/* service cards */
.services{top:634px;height:456px}
.card{position:absolute;top:64px;width:273px;height:347px;background:var(--white);border-radius:16px;box-shadow:0 6px 16px rgba(0,0,0,.14);overflow:hidden;text-align:center}
.card-photo{height:200px;background:linear-gradient(160deg,#7c8a6a,#4d5a45)}
.card h3{font-size:15px;font-weight:400;color:var(--green);margin-top:22px}
.card p{font-size:10px;color:var(--muted);margin:4px 30px 0;line-height:1.5}
.card .btn{left:62px;bottom:25px;width:150px;height:30px;text-transform:none;gap:20px}

/* save time */
.values{top:1090px;height:337px}
.values-mark{left:570px;top:45px}
.values h2{position:absolute;top:128px;width:100%;text-align:center;font-size:20px;font-weight:400;letter-spacing:1px}
.values h2 b{color:var(--green);font-size:14px;margin:0 8px}
.step{position:absolute;top:188px;width:157px;height:62px;background:var(--white);box-shadow:0 3px 10px rgba(0,0,0,.14);display:flex;align-items:center}
.step-icon{width:52px;height:52px;margin:5px;background:var(--green);display:flex;align-items:center;justify-content:center;flex:none}
.step span{font-size:10px;color:var(--muted);padding-left:10px;line-height:1.5}
.step-arrow{position:absolute;top:210px;color:var(--green);font-size:18px}

/* about */
.about{top:1427px;height:618px;background:var(--green);color:var(--white)}
.about-photo{left:600px;top:0;width:600px;height:618px;background:linear-gradient(135deg,#cfcfcf,#6f6f6f 60%,#3a3a3a)}
.about h2{position:absolute;left:0;width:600px;top:110px;text-align:center;font-size:30px;font-weight:400}
.about h2 em{font-style:normal;color:var(--lime)}
.about-text{left:155px;top:160px;width:410px;font-size:11px;line-height:1.8}
.about-text h4{font-size:13px;font-weight:400;margin:20px 0 2px}
.stats{left:155px;top:363px;display:flex}
.stat{width:118px;border-right:1px solid rgba(255,255,255,.6);font-size:8px;line-height:1.3;padding:0 10px}
.stat:first-child{padding-left:0}
.stat:last-child{border-right:none}
.stat .yr{display:block;font-size:9px}
.stat strong{display:block;font-size:34px;font-weight:400;text-align:center;line-height:1.1}
.stat small{display:block;font-size:8px;text-align:center}
.about .btn{top:473px;height:34px;text-transform:none}

/* contact */
.contact{top:2045px;height:667px}
.map{position:absolute;inset:0;background:linear-gradient(135deg,var(--map-a),var(--map-b))}
.contact-card{left:527px;top:60px;width:516px;height:547px;background:var(--white);border-radius:8px;box-shadow:0 6px 20px rgba(0,0,0,.15)}
.contact-card h2{text-align:center;font-size:28px;font-weight:400;margin-top:30px}
.contact-card h2 em{font-style:normal;color:var(--green)}
.field{position:absolute;height:36px;border:1px solid var(--line);border-radius:4px;font-size:11px;color:#aaa;padding:11px 20px}
.checks{position:absolute;left:35px;top:200px;width:445px;height:104px;border:1px solid var(--line);border-radius:4px;padding:12px 20px;font-size:11px;line-height:26px}
.checks i{display:inline-block;width:12px;height:12px;border:1px solid #ccc;margin-right:10px;vertical-align:-1px}
.checks i.on{background:var(--green);border-color:var(--green)}
.submit{left:35px;top:470px;width:445px;height:36px;border-radius:4px;text-transform:none;font-size:13px}

/* pickup */
.pickup{top:2712px;height:553px;background:radial-gradient(circle at 65% 45%,#b6ec62 0,#62c23b 45%,#3f9a32 100%);color:var(--white)}
.pickup-copy{left:155px;top:172px}
.pickup-copy h2{font-size:34px;font-weight:400;line-height:1.15}
.pickup-copy p{font-size:22px;line-height:1.3;margin-top:14px}
.pickup .btn{top:340px;height:38px;text-transform:none}
.truck{left:585px;top:110px;width:460px;height:290px;border-radius:10px;background:linear-gradient(180deg,rgba(255,255,255,.55),rgba(255,255,255,.25))}

/* clients */
.clients{top:3265px;height:383px}
.clients h2{position:absolute;top:80px;width:100%;text-align:center;font-size:28px;font-weight:400}
.clients h2 em{font-style:normal;color:var(--green)}
.client{position:absolute;top:200px;height:60px;display:flex;align-items:center;gap:10px;font-size:26px;font-weight:700;color:var(--ink);white-space:nowrap}
.client i{width:22px;height:22px;background:var(--ink)}
.client-arrow{position:absolute;top:205px;font-size:34px;color:var(--green)}

/* process */
.process{top:3648px;height:557px}
.process-bg{position:absolute;inset:0;background:linear-gradient(160deg,#57b63c,#3e9b2f 55%,#2f7e25)}
.process h2{position:absolute;top:62px;width:100%;text-align:center;font-size:28px;font-weight:400;color:var(--white)}
.pbox{position:absolute;width:98px;height:100px;border-radius:10px;background:var(--white);color:var(--green);font-size:9px;text-align:center;display:flex;flex-direction:column;align-items:center;justify-content:flex-end;padding-bottom:12px;line-height:1.2}
.pbox.fill{background:var(--green);color:var(--white);border:1px solid rgba(255,255,255,.4)}
.chev{position:absolute;width:18px;height:18px;border-radius:50%;background:var(--white);color:var(--green);font-size:11px;display:flex;align-items:center;justify-content:center}

/* footer */
.site-footer{top:4205px;height:437px;background:var(--footer);color:#d8d8d8}
.site-footer h5{font-size:12px;font-weight:700;color:var(--green);letter-spacing:.5px;margin-bottom:14px}
.fcol{font-size:9.5px;line-height:1.9}
.fcol ul{list-style:none}
.fdiv{top:45px;width:1px;height:170px;background:#555}
.badge{top:285px;height:60px;background:#5a5a5a}
.copy{left:0;top:407px;width:1200px;height:30px;background:var(--footer-deep);font-size:9px;color:#aaa;text-align:center;line-height:30px}
</style>
</head>
<body>

<header class="site-header">
  <div class="abs brand"><span class="brand-dot"></span><span class="brand-name">7 Bright Harbor</span></div>
  <a class="btn top-btn" style="left:581px">Pick Up</a>
  <a class="btn top-btn" style="left:738px;background:var(--green-dark)">Drop Off</a>
  <a class="btn top-btn phone" style="left:893px">
    <svg width="13" height="13" viewBox="0 0 24 24"><path d="M6.6 10.8a15 15 0 006.6 6.6l2.2-2.2c.3-.3.7-.4 1-.2 1.1.4 2.3.6 3.6.6.6 0 1 .4 1 1V20c0 .6-.4 1-1 1A17 17 0 013 4c0-.6.4-1 1-1h3.5c.6 0 1 .4 1 1 0 1.3.2 2.5.6 3.6.1.3 0 .7-.2 1z" fill="#47a93a"/></svg>
    (206) 555-0148</a>
</header>

<nav class="main-nav">
  <ul>
    <li>IT Asset Disposition</li>
    <li>Electronics Recycling ⌄</li>
    <li>Secure Data Destruction</li>
    <li>Product Destruction</li>
    <li>About ⌄</li>
    <li>Contact Us</li>
  </ul>
  <a class="btn live-chat">
    <svg width="16" height="14" viewBox="0 0 24 20"><path d="M2 2h16v11H8l-4 4v-4H2z" fill="#fff"/></svg>Live Chat</a>
</nav>

<section class="hero">
  <div class="hero-photo" role="img" aria-label="Hands holding a glass globe above sunlit grass"></div>
  <div class="abs hero-copy">
    <div class="l1">CERTIFIED</div>
    <div class="l2">E-RECYCLING</div>
    <div class="l3">MADE EASY</div>
    <div class="tag">REUSE &amp; RECYCLE 99.9% OF ALL MATERIALS WE RECEIVE</div>
  </div>
  <a class="btn hero-btn"><svg width="12" height="12" viewBox="0 0 12 12"><circle cx="6" cy="6" r="4.5" fill="none" stroke="#fff" stroke-width="1.5"/></svg>Items We Recycle</a>
</section>

<section class="services">
  <article class="card" style="left:155px">
    <div class="card-photo" role="img" aria-label="Recycling bins beside a stone wall"></div>
    <h3>BIN Program</h3>
    <p>Fill up our Bin at Your Location, when done, we come and pick up!</p>
    <a class="btn">Read More <span>→</span></a>
  </article>
  <article class="card" style="left:463px">
    <div class="card-photo" role="img" aria-label="Worker loading a collection container"></div>
    <h3>Same Day Pickups Available</h3>
    <p>Secure Chain of Custody</p>
    <a class="btn">Read More <span>→</span></a>
  </article>
  <article class="card" style="left:771px">
    <div class="card-photo" role="img" aria-label="Pile of shredded hard drives"></div>
    <h3 style="margin-top:28px">On-site Data Destruction</h3>
    <a class="btn">Read More <span>→</span></a>
  </article>
</section>

<section class="values">
  <svg class="abs values-mark" width="66" height="70" viewBox="0 0 66 70">
    <circle cx="30" cy="40" r="26" fill="none" stroke="#47a93a" stroke-width="3"/>
    <path d="M40 18c6-10 18-12 22-10-2 10-10 18-22 14" fill="none" stroke="#47a93a" stroke-width="3"/>
  </svg>
  <h2>SAVE TIME<b>•</b>SAVE MONEY<b>•</b>SAVE THE PLANET</h2>
  <div class="step" style="left:155px"><div class="step-icon"><svg width="26" height="26" viewBox="0 0 24 24"><path d="M4 14v-2a8 8 0 0116 0v2M4 14h3v5H4zM17 14h3v5h-3z" fill="none" stroke="#fff" stroke-width="2"/></svg></div><span>Quick<br>Response</span></div>
  <div class="step-arrow" style="left:318px">›</div>
  <div class="step" style="left:339px"><div class="step-icon"><svg width="26" height="26" viewBox="0 0 24 24"><rect x="3" y="5" width="18" height="16" fill="none" stroke="#fff" stroke-width="2"/><path d="M3 10h18M8 3v4M16 3v4" stroke="#fff" stroke-width="2"/></svg></div><span>Immediate<br>Scheduling</span></div>
  <div class="step-arrow" style="left:502px">›</div>
  <div class="step" style="left:522px"><div class="step-icon"><svg width="28" height="26" viewBox="0 0 26 24"><path d="M2 6h13v11H2zM15 10h5l4 4v3h-9z" fill="none" stroke="#fff" stroke-width="2"/><circle cx="6" cy="19" r="2" fill="#fff"/><circle cx="19" cy="19" r="2" fill="#fff"/></svg></div><span>On-time<br>Secure Pickup</span></div>
  <div class="step-arrow" style="left:685px">›</div>
  <div class="step" style="left:705px"><div class="step-icon"><svg width="26" height="26" viewBox="0 0 24 24"><path d="M12 3l4 7H8zM4 20l4-7 4 7zM14 20l4-7 4 7z" fill="none" stroke="#fff" stroke-width="2"/></svg></div><span>Certified<br>Recycling<br>Process</span></div>
  <div class="step-arrow" style="left:868px">›</div>
  <div class="step" style="left:887px"><div class="step-icon"><svg width="26" height="26" viewBox="0 0 24 24"><path d="M8 3a5 5 0 015 5c0 4-5 9-5 9s-5-5-5-9a5 5 0 015-5z" fill="none" stroke="#fff" stroke-width="2"/><circle cx="18" cy="18" r="3" fill="none" stroke="#fff" stroke-width="2"/></svg></div><span>Certifications &amp;<br>Asset Tracking<br>Delivered</span></div>
</section>

<section class="about">
  <div class="abs about-photo" role="img" aria-label="Team members sorting electronics in a warehouse, black and white"></div>
  <h2>ABOUT <em>US</em></h2>
  <div class="abs about-text">
    <p>We are here for our community. We help the community by offering<br>free drop-off</p>
    <h4 style="margin-top:30px">TO PUT IT SIMPLY :</h4>
    <p>if there is a cord attached, we can recycle it. From computers to photocopiers to washers and dryers, and far far more… we’ll help you.</p>
    <h4 style="margin-top:30px">POUNDS RECYCLED :</h4>
  </div>
  <div class="abs stats">
    <div class="stat"><span class="yr">2020</span><strong>7</strong><small>MILLION POUNDS</small></div>
    <div class="stat"><span class="yr">2019</span><strong>6</strong><small>MILLION POUNDS</small></div>
    <div class="stat"><span class="yr">2018</span><strong>5</strong><small>MILLION POUNDS</small></div>
    <div class="stat"><span class="yr">2017</span><strong>4</strong><small>MILLION POUNDS</small></div>
  </div>
  <a class="btn" style="left:155px;width:145px;background:var(--lime)">About Us</a>
  <a class="btn" style="left:307px;width:136px;border:1.5px solid #fff">Items We Recycle</a>
</section>

<section class="contact">
  <div class="map" role="img" aria-label="Street map of the local area with a pin marking the facility"></div>
  <form class="abs contact-card">
    <h2>CONTACT <em>US</em></h2>
    <div class="field" style="left:35px;top:88px;width:215px">Name</div>
    <div class="field" style="left:265px;top:88px;width:215px">Phone</div>
    <div class="field" style="left:35px;top:144px;width:445px">Email</div>
    <div class="checks">
      <div><i class="on"></i>Electronics Recycling</div>
      <div><i></i>Equipment &amp; Product Destruction</div>
      <div><i></i>Secure Data Destruction</div>
      <div><i></i>IT Asset Disposition</div>
    </div>
    <div class="field" style="left:35px;top:338px;width:445px;height:118px">Message</div>
    <a class="btn submit">Submit</a>
  </form>
</section>

<section class="pickup">
  <div class="abs pickup-copy">
    <h2>SAVE TIME<br>AND DISPOSAL COSTS.</h2>
    <p>WE PICK UP LOADS OF E-WASTE<br>OVER 500 LBS FOR FREE!</p>
  </div>
  <a class="btn" style="left:155px;width:157px;background:var(--lime)">Schedule a Pickup</a>
  <a class="btn" style="left:322px;width:154px;border:1.5px solid #fff">Items We Recycle</a>
  <div class="abs truck" role="img" aria-label="White box truck with company branding"></div>
</section>

<section class="clients">
  <h2>OUR LOCAL <em>CLIENTS</em></h2>
  <div class="client-arrow" style="left:97px">‹</div>
  <div class="client" style="left:168px">Northwind</div>
  <div class="client" style="left:362px;font-size:22px">Skyline Air</div>
  <div class="client" style="left:585px;font-size:24px"><i></i>Cedarview City</div>
  <div class="client" style="left:900px;font-size:22px">Harbor Roast</div>
  <div class="client-arrow" style="left:1085px">›</div>
</section>

<section class="process">
  <div class="process-bg" role="img" aria-label="Seedling and globe on a soft green background"></div>
  <h2>OUR PROCESS</h2>
  <svg class="abs" style="left:0;top:0" width="1200" height="557">
    <g stroke="#fff" stroke-width="2.5" fill="#fff">
      <line x1="495" y1="270" x2="580" y2="225"/><polygon points="585,222 572,222 578,232"/>
      <line x1="495" y1="325" x2="580" y2="370"/><polygon points="585,373 572,373 578,363"/>
      <line x1="763" y1="262" x2="763" y2="312"/><polygon points="757,312 769,312 763,322"/>
      <line x1="990" y1="262" x2="990" y2="312"/><polygon points="984,312 996,312 990,322"/>
    </g>
  </svg>
  <div class="pbox" style="left:158px;top:242px">ON-SITE<br>COLLECTION</div>
  <div class="chev" style="left:250px;top:283px">›</div>
  <div class="pbox fill" style="left:272px;top:242px">SECURE<br>TRANSPORT</div>
  <div class="chev" style="left:364px;top:283px">›</div>
  <div class="pbox" style="left:388px;top:242px">SORTING</div>

  <div class="pbox fill" style="left:598px;top:157px">DATA BEARING<br>DEVICES</div>
  <div class="chev" style="left:690px;top:198px">›</div>
  <div class="pbox" style="left:713px;top:157px">DATA<br>DESTRUCTION</div>
  <div class="chev" style="left:805px;top:198px">›</div>
  <div class="pbox fill" style="left:828px;top:157px">REFURBISH</div>
  <div class="chev" style="left:920px;top:198px">›</div>
  <div class="pbox" style="left:941px;top:157px">REMARKET</div>

  <div class="pbox fill" style="left:598px;top:327px">NON-DATA<br>BEARING DEVICES</div>
  <div class="chev" style="left:690px;top:368px">›</div>
  <div class="pbox" style="left:713px;top:327px">DISMANTLE &amp;<br>PROCESS</div>
  <div class="chev" style="left:805px;top:368px">›</div>
  <div class="pbox fill" style="left:828px;top:327px">RECYCLE</div>
  <div class="chev" style="left:920px;top:368px">›</div>
  <div class="pbox" style="left:941px;top:327px">REPORTING</div>
</section>

<footer class="site-footer">
  <div class="abs brand" style="top:80px"><span class="brand-dot"></span><span class="brand-name">7 Bright Harbor</span></div>
  <div class="abs fcol" style="left:155px;top:195px">
    <h5>CONNECT WITH US</h5>
    <p>212 Cedar Way North<br>Suite B<br>Kent, WA 98032<br>USA</p>
    <p style="margin-top:6px">(206) 555-0148</p>
    <p style="margin-top:6px">(800) 555-0193</p>
  </div>
  <div class="abs fdiv" style="left:370px"></div>
  <div class="abs fcol" style="left:396px;top:45px;width:150px">
    <h5>OUR PROMISE</h5>
    <p>To provide E-Waste Recycling to EVERYONE!</p>
  </div>
  <div class="abs fdiv" style="left:618px"></div>
  <div class="abs fcol" style="left:643px;top:45px;width:210px">
    <h5>OUR MISSION</h5>
    <p>We are a socially conscious recycling company that's fully committed to helping community, including small &amp; large business, with a one-stop solution for the responsible disposal of E-Waste.</p>
    <p style="margin-top:8px">Local and Sustainable<br>0% waste<br>0% landfill<br>100% Environmental Conscious!</p>
  </div>
  <div class="abs fdiv" style="left:925px"></div>
  <div class="abs fcol" style="left:952px;top:45px">
    <h5>SITEMAP</h5>
    <ul><li>Home</li><li>How It Works</li><li>Environment</li><li>Community</li><li>About</li><li>FAQs</li><li>Blog</li><li>Contact</li><li>Request a Pickup</li></ul>
  </div>
  <div class="abs" style="left:405px;top:300px;color:var(--green);font-size:22px">‹</div>
  <div class="abs badge" style="left:445px;width:65px;border-radius:50%"></div>
  <div class="abs badge" style="left:550px;width:68px"></div>
  <div class="abs badge" style="left:655px;width:170px;border-radius:6px"></div>
  <div class="abs badge" style="left:860px;width:60px;border-radius:50%"></div>
  <div class="abs" style="left:1032px;top:300px;color:var(--green);font-size:22px">›</div>
  <div class="abs copy">©Copyright 2021 • 7 Bright Harbor • All Rights Reserved<span style="position:absolute;right:155px">Privacy Policy</span></div>
</footer>

</body>
</html>
```